Rewards Card Design Project

We require a rewards card design for an Indian cuisine restaurant. We wish to keep the design somewhat simple and also professional. We have uploaded the relevant artwork and you may use any of it in the design. The design should include restaurant logo, phone number, address and website address and should include words "rewards card". (The restaurant details are included in the uploaded files). Also we wish the design to be in a format suitable for printing e.g. Adobe Air, CorelDraw etc

Thank you for sending your designs. We've really liked few of them but will wait until end of this week before making final selection. We wish to inform that all designs should be in landscape mode. We intend to print it on cards which are equal in size to standard credit cards (85.60 mm × 53.98 mm). Please also consider the bleeding area while making the designs.

Restaurant

```html
<!DOCTYPE html>
<html lang="en">
<head>
<meta charset="utf-8">
<title>Saffron Hill Rewards Card</title>
<link href="https://fonts.googleapis.com/css2?family=Source+Sans+3:wght@600;700&family=Sacramento&family=Arimo&display=swap" rel="stylesheet">
<style>
  :root {
    --page: #ffffff;
    --card-dark: #231f20;
    --gold: #c9a063;
    --gold-soft: #d4aa6a;
    --white: #ffffff;
    --caption: #333333;
    --photo-blue: #3b3f78;
    --photo-brown: #5a3a22;
    --photo-warm: #b06a2a;
  }
  html, body {
    margin: 0;
    width: 1200px;
    height: 1200px;
    overflow: hidden;
    background: var(--page);
  }
  .canvas {
    position: relative;
    width: 1200px;
    height: 1200px;
  }
  .card {
    position: absolute;
    left: 95px;
    top: 282px;
    width: 1010px;
    height: 636px;
    background: var(--card-dark);
    overflow: hidden;
  }
  .card__photo {
    position: absolute;
    left: 420px;
    top: 0;
    width: 590px;
    height: 636px;
    background:
      radial-gradient(ellipse 260px 180px at 420px 350px, var(--photo-warm) 0%, rgba(176,106,42,0.5) 45%, transparent 75%),
      radial-gradient(ellipse 380px 260px at 380px 480px, rgba(140,110,80,0.6) 0%, transparent 70%),
      linear-gradient(160deg, var(--photo-brown) 0%, var(--photo-blue) 40%, #2e2c4a 60%, var(--photo-brown) 100%);
    -webkit-mask-image: linear-gradient(90deg, transparent 0%, #000 35%);
    mask-image: linear-gradient(90deg, transparent 0%, #000 35%);
  }
  .card__border {
    position: absolute;
    left: 0;
    width: 1010px;
    height: 22px;
    background: linear-gradient(90deg, var(--gold) 0%, #e0bd80 50%, var(--gold) 100%);
    opacity: 0.85;
  }
  .card__border--top { top: 33px; }
  .card__border--bottom { top: 582px; }
  .brand {
    position: absolute;
    left: 80px;
    top: 96px;
    display: flex;
    align-items: center;
    gap: 18px;
    font-family: "Source Sans 3", sans-serif;
    font-weight: 700;
    font-size: 72px;
    color: var(--gold-soft);
    line-height: 1;
  }
  .brand__mark {
    width: 40px;
    height: 40px;
    background: var(--gold-soft);
  }
  .card__title {
    position: absolute;
    left: 80px;
    top: 280px;
    margin: 0;
    font-family: "Sacramento", cursive;
    font-weight: 400;
    font-size: 92px;
    color: var(--white);
    line-height: 1;
  }
  .contact {
    position: absolute;
    left: 78px;
    top: 424px;
    font-family: "Source Sans 3", sans-serif;
    font-weight: 700;
    color: var(--white);
  }
  .contact__web { font-size: 30px; margin: 0 0 12px; }
  .contact__line { font-size: 26px; margin: 0 0 8px; }
  .caption {
    position: absolute;
    top: 982px;
    left: 0;
    width: 1200px;
    text-align: center;
    font-family: "Arimo", sans-serif;
    font-size: 38px;
    color: var(--caption);
  }
</style>
</head>
<body>
<div class="canvas">
  <section class="card">
    <div class="card__photo" role="img" aria-label="Photograph of a plated Indian curry dish with vegetables"></div>
    <div class="card__border card__border--top" role="img" aria-label="Gold ornamental border pattern"></div>
    <div class="card__border card__border--bottom" role="img" aria-label="Gold ornamental border pattern"></div>
    <div class="brand"><span class="brand__mark"></span><span>Saffron Hill</span></div>
    <h1 class="card__title">Rewards Card</h1>
    <div class="contact">
      <p class="contact__web">www.SaffronHill.com.au</p>
      <p class="contact__line">Dine In • Take-Away • Home Delivery</p>
      <p class="contact__line">Ph. 9000 1234 • 12 Elm Street, Northvale</p>
    </div>
  </section>
  <div class="caption">85.6 x 53.98 mm</div>
</div>
</body>
</html>
```